Velora Pedalworks

We are a new start up company selling (online) innovative cycling products.
Being a new player in the market a modern eye catching logo would be good.
Initially selling safety tail lights with blinkers & modern designed cycling gloves and eventually extending our range into cycling clothing. Many of our products will have a safety theme.

Please see logo attached.

Reason: I have extended deadline because i have just received the Logo to be used.

Target Market(s)

We will be target marketing to the young 20-30year old trendy commuter cyclists to the 40 - 60 year old weekend road riders with there immaculate color coordinated road bikes & clothing.

Industry/Entity Type

Safety

Requirements
Must have
• Name: Mavin Tolby
Line for Mobile No. 0438 261 905
Line for email Address: mavin@velorapedalworks.example.com.au
3 Lines for Postal Address: PO Box 3862
Wattle Crest Corner
NSW 2174
Website: www.velorapedalworks.example.com.au

```html
<!DOCTYPE html>
<html lang="en">
<head>
<meta charset="utf-8">
<title>Velora Pedalworks – Business Card</title>
<link rel="stylesheet" href="https://fonts.googleapis.com/css2?family=Open+Sans:wght@400;600;700&display=swap">
<style>
  :root {
    --backdrop: #d6d6d6;
    --paper: #ffffff;
    --ink: #231f20;
    --accent: #f7841f;
    --panel-top: #1f2022;
    --panel-bottom: #0f1011;
    --text-light: #f2f2f2;
    --divider: #d9d9d9;
  }
  * { box-sizing: border-box; margin: 0; padding: 0; }
  html, body {
    width: 1200px; height: 900px; overflow: hidden;
    background: var(--backdrop);
    font-family: "Open Sans", Arial, sans-serif;
  }
  .card {
    position: absolute; left: 160px; top: 200px;
    width: 880px; height: 500px;
    border-radius: 36px; overflow: hidden;
    background: var(--paper);
    display: flex; flex-direction: column;
  }
  .card__brand {
    height: 280px;
    display: flex; align-items: center; justify-content: center;
    gap: 18px; padding-top: 20px;
  }
  .brand__dot {
    width: 34px; height: 34px; border-radius: 50%;
    background: var(--accent);
  }
  .brand__name {
    font-size: 56px; font-weight: 700; letter-spacing: -1.5px;
    color: var(--ink);
  }
  .card__stripe { height: 16px; background: var(--accent); }
  .card__details {
    flex: 1; position: relative;
    background: linear-gradient(180deg, var(--panel-top), var(--panel-bottom));
  }
  .person {
    position: absolute; right: 500px; top: 66px; text-align: right;
  }
  .person__name {
    font-size: 32px; font-weight: 600; color: var(--accent); line-height: 1.15;
  }
  .person__role { font-size: 20px; color: var(--text-light); }
  .details__divider {
    position: absolute; left: 400px; top: 26px;
    width: 2px; height: 158px; background: var(--divider);
  }
  .contact-list {
    position: absolute; left: 420px; top: 22px;
    list-style: none; color: var(--text-light);
    font-size: 20px; line-height: 30px;
  }
  .contact-list li { display: flex; align-items: flex-start; gap: 8px; }
  .contact-list svg { width: 22px; height: 22px; margin-top: 4px; flex: none; fill: var(--accent); }
  .contact-list .address { display: flex; flex-direction: column; }
</style>
</head>
<body>
  <main class="card">
    <header class="card__brand">
      <span class="brand__dot"></span>
      <span class="brand__name">Velora Pedalworks</span>
    </header>
    <div class="card__stripe"></div>
    <section class="card__details">
      <div class="person">
        <p class="person__name">Mavin Tolby</p>
        <p class="person__role">Manager</p>
      </div>
      <div class="details__divider"></div>
      <ul class="contact-list">
        <li>
          <svg viewBox="0 0 24 24" aria-hidden="true"><path d="M6.6 10.8a15.1 15.1 0 0 0 6.6 6.6l2.2-2.2a1 1 0 0 1 1-.25 11.4 11.4 0 0 0 3.6.57 1 1 0 0 1 1 1V20a1 1 0 0 1-1 1A17 17 0 0 1 3 4a1 1 0 0 1 1-1h3.5a1 1 0 0 1 1 1c0 1.25.2 2.45.57 3.57a1 1 0 0 1-.25 1z"/></svg>
          <span>0438 261 905</span>
        </li>
        <li>
          <svg viewBox="0 0 24 24" aria-hidden="true"><path d="M12 2a10 10 0 1 0 0 20 10 10 0 0 0 0-20zm6.9 6h-2.9a15.7 15.7 0 0 0-1.4-3.6A8 8 0 0 1 18.9 8zM12 4c.8 1.2 1.5 2.5 1.9 4h-3.8c.4-1.5 1.1-2.8 1.9-4zM4.3 14a8.2 8.2 0 0 1 0-4h3.4a16.5 16.5 0 0 0 0 4zm.8 2h2.9c.3 1.3.8 2.5 1.4 3.6A8 8 0 0 1 5.1 16zM8 8H5.1a8 8 0 0 1 4.3-3.6C8.8 5.5 8.3 6.7 8 8zm4 12c-.8-1.2-1.5-2.5-1.9-4h3.8c-.4 1.5-1.1 2.8-1.9 4zm2.3-6H9.7a14.7 14.7 0 0 1 0-4h4.6a14.7 14.7 0 0 1 0 4zm.3 5.6c.6-1.1 1.1-2.3 1.4-3.6h2.9a8 8 0 0 1-4.3 3.6zm1.7-5.6a16.5 16.5 0 0 0 0-4h3.4a8.2 8.2 0 0 1 0 4z"/></svg>
          <span>www.velorapedalworks.example.com.au</span>
        </li>
        <li>
          <svg viewBox="0 0 24 24" aria-hidden="true"><path d="M3 5h18a1 1 0 0 1 1 1v12a1 1 0 0 1-1 1H3a1 1 0 0 1-1-1V6a1 1 0 0 1 1-1zm1 2.2V17h16V7.2l-8 5.3z"/></svg>
          <span>mavin@velorapedalworks.example.com.au</span>
        </li>
        <li>
          <svg viewBox="0 0 24 24" aria-hidden="true"><path d="M12 3l10 9h-3v9h-5v-6h-4v6H5v-9H2z"/></svg>
          <span class="address"><span>PO Box 3862</span><span>Wattle Crest Corner</span></span>
        </li>
      </ul>
    </section>
  </main>
</body>
</html>
```